HOLTMARK Construction Services
Project: Stationary
Stationary
Simple
Derek Pannell
derek@hltservices-example.com
www.hltservices-example.com
Finalized Draft of the logo can be seen on the following URL: http://www.quillora-example.com/contests/business-logo-264. AI file will be uploaded soon. At the front of the business card the following text should be added design.engineer.build commercial.residential

```html
<!DOCTYPE html>
<html lang="en">
<head>
<meta charset="utf-8">
<title>HOLTMARK Construction Services – Stationery</title>
<link href="https://fonts.googleapis.com/css2?family=Open+Sans:wght@400;600&display=swap" rel="stylesheet">
<style>
  :root {
    --lime: #8dc63f;
    --ink: #111111;
    --paper: #ffffff;
    --mark-grey: #6d6e71;
    --frame: #b5b5b5;
    --text-grey: #333333;
  }
  * { margin: 0; padding: 0; box-sizing: border-box; }
  html, body { width: 1200px; height: 749px; overflow: hidden; background: var(--paper); }
  body { position: relative; font-family: "Open Sans", Arial, sans-serif; }

  .card {
    position: absolute;
    width: 528px;
    height: 296px;
    border: 1px solid var(--frame);
    overflow: hidden;
  }
  .card--front { left: 67px; top: 62px; background: var(--paper); }
  .card--white { left: 625px; top: 62px; background: var(--paper); }
  .card--black { left: 67px; top: 380px; background: var(--ink); }
  .card--lime  { left: 625px; top: 380px; background: var(--lime); }

  .front-swoosh { position: absolute; inset: 0; width: 100%; height: 100%; }

  .brand { position: absolute; display: flex; flex-direction: column; align-items: center; }
  .brand__dot { border-radius: 50%; background: var(--mark-grey); }
  .brand__name, .brand__sub { font-weight: 600; line-height: 1; }
  .brand__name { letter-spacing: 1px; }
  .brand__sub { letter-spacing: 3px; text-transform: uppercase; margin-top: 6px; }

  .brand--front { left: 18px; top: 22px; align-items: flex-start; }
  .brand--front .brand__dot { width: 62px; height: 62px; margin-left: 24px; margin-bottom: 8px; }
  .brand--front .brand__name { font-size: 30px; color: var(--ink); }
  .brand--front .brand__sub { font-size: 7px; letter-spacing: 2px; color: var(--ink); margin-top: 3px; }

  .brand--center { left: 0; right: 0; top: 58px; }
  .brand--center .brand__dot { width: 96px; height: 96px; margin-bottom: 22px; }
  .brand--center .brand__name { font-size: 44px; }
  .brand--center .brand__sub { font-size: 10px; }

  .card--white .brand__name, .card--white .brand__sub { color: var(--mark-grey); }
  .card--black .brand__name, .card--black .brand__sub { color: var(--paper); }
  .card--black .brand__dot { background: #8a8b8d; }
  .card--lime .brand__name, .card--lime .brand__sub { color: var(--paper); }

  .holder-name {
    position: absolute; left: 298px; top: 162px;
    font-size: 19px; color: var(--lime); font-weight: 400;
  }
  .contact {
    position: absolute; left: 26px; top: 230px;
    list-style: none; color: var(--paper); font-size: 11px; line-height: 15px;
  }
</style>
</head>
<body>

  <section class="card card--front" aria-label="Business card front">
    <svg class="front-swoosh" viewBox="0 0 528 296" preserveAspectRatio="none" aria-hidden="true">
      <path d="M0 150 C 120 205, 330 215, 528 160 L528 296 L0 296 Z" fill="var(--ink)"/>
      <path d="M0 160 C 120 215, 330 225, 528 172 L528 296 L0 296 Z" fill="var(--lime)"/>
    </svg>
    <div class="brand brand--front">
      <span class="brand__dot"></span>
      <span class="brand__name">HOLTMARK</span>
      <span class="brand__sub">Construction Services</span>
    </div>
    <p class="holder-name">Derek Pannell</p>
    <ul class="contact">
      <li>Phone: 281-555-0147</li>
      <li>Email: derek@hltservices-example.com</li>
      <li>www.hltservices-example.com</li>
    </ul>
  </section>

  <section class="card card--white" aria-label="Business card back, white">
    <div class="brand brand--center">
      <span class="brand__dot"></span>
      <span class="brand__name">HOLTMARK</span>
      <span class="brand__sub">Construction Services</span>
    </div>
  </section>

  <section class="card card--black" aria-label="Business card back, black">
    <div class="brand brand--center">
      <span class="brand__dot"></span>
      <span class="brand__name">HOLTMARK</span>
      <span class="brand__sub">Construction Services</span>
    </div>
  </section>

  <section class="card card--lime" aria-label="Business card back, green">
    <div class="brand brand--center">
      <span class="brand__dot"></span>
      <span class="brand__name">HOLTMARK</span>
      <span class="brand__sub">Construction Services</span>
    </div>
  </section>

</body>
</html>
```